タイトルは『集い準備応援戦団 ホール任せマン 集い段取り快勝手引きブック」とします。表紙、タイトルには戦隊もののヒーローを彷彿とさせるようなデザインを希望します。

ゴルフコンペの幹事業務がどんな内容なのかを細かく丁寧に説明し、尚且つ弊社のサービスがどんなメリットがあるのかを事細かに説明する内容です。サービスの概要を伝える見開き2ページの漫画と、詳細を記したデータを貼付します。

①表紙→②漫画→③詳細

このうち①、③を合わせてお願いしたいと思います。貼付内容の著作権は弊社にありますので、パンフレット内で画像等自由に使用してください。

ページ数に拘りはないのでわかりやすい内容にするために増えてしまっても問題ないです。

当方のコンセプトをよく理解し、さらに発展させてくれました。やりとりの中で当方の漠然としたイメージがどんどん具体化していき気持ちよかったです。最終的には12ページに渡る非常に素晴らしいものを納品していただきました。

確定が遅くなり申し訳ございませんでした。どれも素晴らしいご提案でした。また機会がありましたら宜しくお願い致します。

```html
<!DOCTYPE html>
<html lang="ja">
<head>
<meta charset="utf-8">
<title>集い段取り快勝手引きブック</title>
<link href="https://fonts.googleapis.com/css2?family=Dela+Gothic+One&family=M+PLUS+1p:wght@800;900&display=swap" rel="stylesheet">
<style>
  :root {
    --red: #e60012;
    --deep-red: #b5000e;
    --white: #ffffff;
    --ink: #1a1a1a;
    --ray-red: #e8262e;
    --ray-orange: #f39121;
    --ray-yellow: #fff000;
    --ray-green: #3cb043;
    --ray-cyan: #1fb6e6;
    --ray-blue: #1d4fa8;
    --ray-purple: #7b2d8e;
    --ray-pink: #e4257d;
    --ground: #c9c9c9;
  }
  * { margin: 0; padding: 0; box-sizing: border-box; }
  html, body { width: 837px; height: 1200px; overflow: hidden; background: var(--white); }
  .cover {
    position: relative; width: 837px; height: 1200px; overflow: hidden;
    background: var(--white);
    font-family: "M PLUS 1p", sans-serif;
  }
  .top-band {
    position: absolute; top: 0; left: 0; width: 100%; height: 62px;
    background: var(--red); color: var(--white);
    display: flex; align-items: center; justify-content: center;
    font-weight: 900; font-size: 34px; letter-spacing: 2px;
  }
  .top-band .keep {
    position: absolute; right: 22px; bottom: 12px; font-size: 20px;
  }
  .sunburst { position: absolute; left: 0; top: 250px; width: 837px; height: 950px; }
  .title-block {
    position: absolute; top: 92px; left: 0; width: 100%; text-align: center; z-index: 3;
  }
  .title-sub {
    display: inline-block; background: var(--red); color: var(--white);
    font-family: "Dela Gothic One", sans-serif; font-size: 42px; line-height: 1;
    padding: 8px 26px 10px; letter-spacing: 3px;
    clip-path: polygon(3% 0, 97% 0, 100% 100%, 0 100%);
  }
  .title-main {
    margin-top: 6px;
    font-family: "Dela Gothic One", sans-serif; font-size: 108px; line-height: 1.05;
    color: var(--red); letter-spacing: 2px;
    -webkit-text-stroke: 10px var(--white); paint-order: stroke fill;
    text-shadow: 0 0 0 var(--white), 4px 6px 0 var(--deep-red);
    transform: skewX(-6deg);
  }
  .ray-label {
    position: absolute; z-index: 2;
    writing-mode: vertical-rl; text-orientation: upright;
    font-weight: 900; font-size: 46px; color: var(--white); letter-spacing: 2px;
    text-shadow: 0 0 6px rgba(0,0,0,.35);
    transform-origin: center bottom;
  }
  .bubble {
    position: absolute; left: 175px; top: 700px; width: 490px; height: 118px; z-index: 3;
  }
  .bubble-text {
    position: absolute; left: 0; top: 0; width: 100%; height: 100%;
    display: flex; align-items: center; justify-content: center;
    font-weight: 900; font-size: 50px; color: var(--ink);
  }
  .heroes {
    position: absolute; left: 90px; top: 835px; width: 657px; height: 320px; z-index: 2;
    background: linear-gradient(180deg, #3a3a3a 0%, #222 60%, #111 100%);
    border-radius: 60px 60px 10px 10px;
  }
  .ground {
    position: absolute; left: 60px; top: 1140px; width: 717px; height: 28px;
    background: radial-gradient(ellipse at center, var(--ground) 0%, rgba(201,201,201,0) 70%);
  }
</style>
</head>
<body>
<div class="cover">
  <header class="top-band">集い段取り快勝手引きブック<span class="keep">保存版</span></header>

  <svg class="sunburst" viewBox="0 0 837 950" aria-hidden="true">
    <g transform="translate(418 640)">
      <polygon points="0,0 -900,250 -900,-60" fill="var(--ray-pink)"/>
      <polygon points="0,0 -900,-60 -900,-500" fill="var(--ray-red)"/>
      <polygon points="0,0 -900,-500 -520,-900" fill="var(--ray-orange)"/>
      <polygon points="0,0 -520,-900 -160,-900" fill="var(--ray-yellow)"/>
      <polygon points="0,0 -160,-900 160,-900" fill="var(--ray-green)"/>
      <polygon points="0,0 160,-900 520,-900" fill="var(--ray-cyan)"/>
      <polygon points="0,0 520,-900 900,-500" fill="var(--ray-blue)"/>
      <polygon points="0,0 900,-500 900,-60" fill="var(--ray-purple)"/>
      <polygon points="0,0 900,-60 900,250" fill="var(--ray-pink)"/>
    </g>
    <rect x="0" y="0" width="837" height="60" fill="url(#fade)"/>
    <defs>
      <linearGradient id="fade" x1="0" y1="0" x2="0" y2="1">
        <stop offset="0" stop-color="#fff"/>
        <stop offset="1" stop-color="#fff" stop-opacity="0"/>
      </linearGradient>
    </defs>
  </svg>

  <div class="title-block">
    <div class="title-sub">集い準備応援戦団</div>
    <div class="title-main">ホール任せマン</div>
  </div>

  <span class="ray-label" style="left:48px;top:500px;transform:rotate(-28deg)">送迎</span>
  <span class="ray-label" style="left:120px;top:345px;transform:rotate(-20deg)">パーティー</span>
  <span class="ray-label" style="left:262px;top:380px;transform:rotate(-10deg)">賞品</span>
  <span class="ray-label" style="left:390px;top:300px;transform:rotate(-2deg)">プレー内容</span>
  <span class="ray-label" style="left:520px;top:360px;transform:rotate(8deg)">ご予算</span>
  <span class="ray-label" style="left:630px;top:330px;transform:rotate(16deg)">開催日</span>
  <span class="ray-label" style="left:735px;top:370px;transform:rotate(24deg)">参加費</span>

  <div class="bubble">
    <svg width="490" height="118" viewBox="0 0 490 118" aria-hidden="true">
      <path d="M245 4 C380 4 486 22 486 56 C486 88 400 104 290 106 L262 116 L250 106 C110 104 4 88 4 56 C4 22 110 4 245 4 Z"
            fill="var(--white)" stroke="var(--ink)" stroke-width="4"/>
    </svg>
    <div class="bubble-text">お任せください!!</div>
  </div>

  <div class="ground"></div>
  <div class="heroes" role="img" aria-label="黒いスーツと色付きサングラス姿で敬礼する4人の戦団メンバーのイラスト"></div>
</div>
</body>
</html>
```